Title Company
Stationary for Title Company
Project: Title Company
Title Company  - Real Estate
Creative Brief
Professional
Tobias Renwald
4810 Larkspur Way Suite 210 Fenwick Bay, Fl. 33990
tobiasrenwald@quillmarsh.com
www.harrowfieldrealestategroup.com

```html
<!DOCTYPE html>
<html lang="en">
<head>
<meta charset="utf-8">
<title>Brambleoak Deeds — Stationery</title>
<link href="https://fonts.googleapis.com/css2?family=Cinzel:wght@600&family=Open+Sans:wght@400;600&display=swap" rel="stylesheet">
<style>
  :root {
    --backdrop: #f4f5f7;
    --paper: #ffffff;
    --edge: #e2e5ea;
    --brand: #1d4f80;
    --brand-deep: #123a63;
    --brand-light: #3f82bf;
    --ink-soft: #6b7480;
    --mark-faint: #dde8f3;
  }
  * { margin: 0; padding: 0; box-sizing: border-box; }
  html, body { width: 1200px; height: 936px; overflow: hidden; }
  body {
    position: relative;
    background: var(--backdrop);
    font-family: "Open Sans", Arial, sans-serif;
    color: var(--ink-soft);
  }
  .sheet {
    position: absolute;
    background: var(--paper);
    border: 1px solid var(--edge);
  }
  .wordmark {
    display: flex;
    align-items: center;
    gap: 8px;
    font-family: "Cinzel", Georgia, serif;
    font-weight: 600;
    color: var(--brand);
    white-space: nowrap;
    letter-spacing: 0.04em;
  }
  .wordmark .mark-square {
    display: inline-block;
    flex: none;
    background: var(--brand);
  }
  .faint-square {
    position: absolute;
    background: var(--mark-faint);
  }

  /* Letterhead */
  .letterhead { left: 254px; top: 63px; width: 317px; height: 546px; }
  .letterhead .wordmark { position: absolute; top: 34px; left: 0; right: 0; justify-content: center; font-size: 15px; }
  .letterhead .wordmark .mark-square { width: 12px; height: 12px; }
  .letterhead .faint-square { left: 126px; top: 222px; width: 66px; height: 66px; }
  .letterhead-footer {
    position: absolute; left: 10px; right: 10px; bottom: 18px;
    display: flex; justify-content: center; gap: 8px;
    font-size: 5px; line-height: 1.4; white-space: nowrap;
  }

  /* Folder */
  .folder { left: 634px; top: 38px; width: 462px; height: 609px; }
  .folder .wordmark { position: absolute; top: 302px; left: 0; right: 0; justify-content: center; font-size: 30px; gap: 12px; }
  .folder .wordmark .mark-square { width: 24px; height: 24px; }

  /* Business card front */
  .card-front { left: 43px; top: 672px; width: 180px; height: 89px; }
  .card-front .wordmark { position: absolute; top: 16px; left: 0; right: 0; justify-content: center; font-size: 9px; gap: 5px; }
  .card-front .wordmark .mark-square { width: 7px; height: 7px; }
  .card-person { position: absolute; top: 46px; left: 0; right: 0; text-align: center; }
  .card-person .name { font-size: 7px; font-weight: 600; color: var(--brand-deep); letter-spacing: 0.08em; text-transform: uppercase; }
  .card-person .role { font-size: 5px; margin-top: 2px; }

  /* Business card back */
  .card-back { left: 43px; top: 786px; width: 180px; height: 92px; overflow: hidden; }
  .card-back .faint-square { left: 26px; top: 16px; width: 60px; height: 60px; }

  /* Envelope front */
  .envelope-front { left: 266px; top: 672px; width: 432px; height: 206px; }
  .envelope-front .wordmark { position: absolute; top: 22px; left: 24px; font-size: 12px; }
  .envelope-front .wordmark .mark-square { width: 10px; height: 10px; }
  .return-address { position: absolute; top: 48px; left: 24px; font-size: 5.5px; white-space: nowrap; }

  /* Envelope back */
  .envelope-back { left: 736px; top: 672px; width: 431px; height: 206px; overflow: hidden; }
  .envelope-flap {
    position: absolute; left: 0; top: 0; width: 100%; height: 78px;
    background: linear-gradient(180deg, var(--brand-light) 0%, var(--brand) 55%, var(--brand-deep) 100%);
    display: flex; align-items: center; justify-content: center;
  }
  .envelope-flap .web {
    color: #ffffff; font-size: 8px; letter-spacing: 0.28em; text-transform: uppercase; white-space: nowrap;
  }
  .envelope-back svg { position: absolute; left: 0; top: 78px; }
</style>
</head>
<body>

  <section class="sheet letterhead">
    <div class="wordmark"><span class="mark-square"></span>Brambleoak Deeds</div>
    <div class="faint-square"></div>
    <div class="letterhead-footer">
      <span>305.555.0142</span>
      <span>4810 Larkspur Way Suite 210 Fenwick Bay, Fl. 33990</span>
      <span>tobiasrenwald@quillmarsh.com</span>
      <span>305.555.0187</span>
    </div>
  </section>

  <section class="sheet folder">
    <div class="wordmark"><span class="mark-square"></span>Brambleoak Deeds</div>
  </section>

  <section class="sheet card-front">
    <div class="wordmark"><span class="mark-square"></span>Brambleoak Deeds</div>
    <div class="card-person">
      <div class="name">Tobias Renwald</div>
      <div class="role">Closing Agent</div>
    </div>
  </section>

  <section class="sheet card-back">
    <div class="faint-square"></div>
  </section>

  <section class="sheet envelope-front">
    <div class="wordmark"><span class="mark-square"></span>Brambleoak Deeds</div>
    <div class="return-address">4810 Larkspur Way Suite 210 Fenwick Bay, Fl. 33990</div>
  </section>

  <section class="sheet envelope-back">
    <div class="envelope-flap"><span class="web">www.harrowfieldrealestategroup.com</span></div>
    <svg width="431" height="128" viewBox="0 0 431 128" aria-hidden="true">
      <path d="M0 128 L215 40 L431 128" fill="none" stroke="#e6e9ee" stroke-width="1"/>
    </svg>
  </section>

</body>
</html>
```